diesel mechanic business card design

stalwart diesel is a new and upcoming business we are looking for some bad ass designs to help get us started we offer 24 hour road service, off road recovery, welding and custom fabrications we are diesel mechanics so our design should be bold and eye catching flames wrenches engine parts are cool we work in an industrial environment around heavy trucks and equipment this in not a quikko slick we fix it all nothing is to big or to small the colors red and black are always a plus but we are open to anything you guys can come up with ready set go

Target Market(s)

other small business primarily trucking and transportation companys

Industry/Entity Type

Business

Contact Information for Business Card

company name Stalwert diesel truck & trailer repair / address 14 rear north benton ave dunmere OH 43530 / ownersAdam DeLuccie 570-614-3385 / Curtis Vanholm 570-248-7731 E mail owenmarcotti@fieldpost.example fax 570-692-1856

Requirements
Nice to have
• industrial modern design
Should not have
• rainbows butterfly's unicorns or cupcakes

```html
<!DOCTYPE html>
<html lang="en">
<head>
<meta charset="utf-8">
<title>Stalwert diesel truck &amp; trailer repair — business card</title>
<link href="https://fonts.googleapis.com/css2?family=Ubuntu:wght@500;700&display=swap" rel="stylesheet">
<style>
  :root {
    --brand-red: #bb1f26;
    --ink: #111111;
    --paper: #ffffff;
    --backdrop: #ece9e4;
    --frame-line: #c9c9c9;
  }
  * { box-sizing: border-box; margin: 0; padding: 0; }
  html, body {
    width: 1189px; height: 1200px; overflow: hidden;
    background: var(--backdrop);
    font-family: "Ubuntu", sans-serif;
  }
  .card {
    position: absolute; left: 171px;
    width: 855px; height: 488px;
    box-shadow: 6px 8px 14px rgba(0,0,0,.28);
  }
  .card--front { top: 67px; background: var(--paper); }
  .card--back { top: 627px; background: var(--brand-red); }

  .brand { position: absolute; line-height: 1; }
  .brand__name { font-weight: 700; letter-spacing: 1.5px; }
  .brand__tagline { font-weight: 700; }

  .card--front .brand { left: 49px; top: 42px; }
  .card--front .brand__name { font-size: 74px; color: var(--brand-red); }
  .card--front .brand__tagline { font-size: 31px; color: var(--ink); margin-top: 0; letter-spacing: .3px; }

  .contacts { position: absolute; left: 561px; top: 40px; }
  .contact__name { font-weight: 700; font-size: 27px; color: var(--brand-red); line-height: 1; }
  .contact__phone {
    display: flex; align-items: center; gap: 12px;
    font-weight: 500; font-size: 23px; color: var(--ink); line-height: 1; margin: 2px 0 10px;
  }
  .contact__phone svg { width: 18px; height: 18px; }

  .info-row {
    position: absolute; top: 170px; left: 49px; right: 50px;
    display: flex; justify-content: space-between;
    font-size: 24px; font-weight: 700; line-height: 1;
  }
  .info-row .label { color: var(--brand-red); }
  .info-row .value { color: var(--ink); }

  .gallery {
    position: absolute; top: 197px; left: 10px; right: 10px;
    display: flex; justify-content: space-between;
  }
  .gallery__frame {
    width: 198px; height: 213px;
    border: 1px solid var(--frame-line); padding: 12px 11px 13px;
    background: var(--paper);
  }
  .gallery__photo { width: 100%; height: 100%; }
  .photo--red-cab { background: linear-gradient(135deg, #c81c22 0%, #a3161b 55%, #6d6d6d 100%); }
  .photo--yellow-engine { background: linear-gradient(160deg, #e6d21e 0%, #8c7a3a 45%, #3b4256 100%); }
  .photo--shop-floor { background: linear-gradient(180deg, #bfbcb6 0%, #8e8a84 55%, #b0aca6 100%); }
  .photo--red-rig { background: linear-gradient(180deg, #d3d3d3 0%, #a1222f 55%, #707070 100%); }

  .address-band {
    position: absolute; left: 0; right: 0; bottom: 0; height: 65px;
    background: var(--brand-red); color: var(--paper);
    display: flex; align-items: center; justify-content: center;
    font-size: 29px; font-weight: 500;
  }

  .card--back .brand {
    left: 0; right: 0; top: 180px; text-align: center; color: var(--paper);
  }
  .card--back .brand__name { font-size: 100px; }
  .card--back .brand__tagline { font-size: 42px; margin-top: 0; }
</style>
</head>
<body>
  <section class="card card--front">
    <div class="brand">
      <div class="brand__name">Stalwert</div>
      <div class="brand__tagline">diesel truck &amp; trailer repair</div>
    </div>

    <div class="contacts">
      <div class="contact__name">Owen Marcotti</div>
      <div class="contact__phone">
        <svg viewBox="0 0 18 18" aria-hidden="true"><rect width="18" height="18" fill="#111"/><path d="M5 3c1 0 1.6 2.4 1.6 3S5.5 7 5.8 8c.5 1.6 2.4 3.6 4 4 .8.2 1.2-.9 1.8-.9s3 .6 3 1.6-1.4 2.3-2.6 2.3C7.2 15 3 10.8 3 6 3 4.4 4 3 5 3z" fill="#fff"/></svg>
        570-614-3385
      </div>
      <div class="contact__name">Curtis Vanholm</div>
      <div class="contact__phone">
        <svg viewBox="0 0 18 18" aria-hidden="true"><rect width="18" height="18" fill="#111"/><path d="M5 3c1 0 1.6 2.4 1.6 3S5.5 7 5.8 8c.5 1.6 2.4 3.6 4 4 .8.2 1.2-.9 1.8-.9s3 .6 3 1.6-1.4 2.3-2.6 2.3C7.2 15 3 10.8 3 6 3 4.4 4 3 5 3z" fill="#fff"/></svg>
        570-248-7731
      </div>
    </div>

    <div class="info-row">
      <div><span class="label">fax</span> <span class="value">570-692-1856</span></div>
      <div><span class="label">E mail:</span> <span class="value">owenmarcotti@fieldpost.example</span></div>
    </div>

    <div class="gallery">
      <div class="gallery__frame"><div class="gallery__photo photo--red-cab" role="img" aria-label="Mechanic working beside the cab of a red truck"></div></div>
      <div class="gallery__frame"><div class="gallery__photo photo--yellow-engine" role="img" aria-label="Mechanic servicing the engine of a yellow truck"></div></div>
      <div class="gallery__frame"><div class="gallery__photo photo--shop-floor" role="img" aria-label="Repair shop floor with trucks and equipment"></div></div>
      <div class="gallery__frame"><div class="gallery__photo photo--red-rig" role="img" aria-label="Red semi tractor parked in a bay"></div></div>
    </div>

    <div class="address-band">14 rear north benton ave dunmere OH 43530</div>
  </section>

  <section class="card card--back">
    <div class="brand">
      <div class="brand__name">Stalwert</div>
      <div class="brand__tagline">diesel truck &amp; trailer repair</div>
    </div>
  </section>
</body>
</html>
```